Book cover design for title:

KITE
Turning Crews into Clans.

Author Marla Voskin

This is my second book the first one is The Hum Building a Flourishing and Cooperative Workplace Growth Climate ( see cover on www.marlavoskin.com).

I am after a cover that echoes the title of The Hum, (ie big bold lettering for the word KITE but not necessarily the images on the front. Although stylised figures are more the style I am after than realist photos. Strong colours and bold statement.

It is about teams that are able to thrive in the complexity of the fast paced and disruptive nature of the world today. 21st century tribes who connect fast to purpose and to each other.

My LinkedIn Marla Voskin and my website give you a flavour of what I do and how I do it.

```html
<!DOCTYPE html>
<html lang="en">
<head>
<meta charset="UTF-8">
<title>KITE – Turning Crews into Clans – Marla Voskin</title>
<link href="https://fonts.googleapis.com/css2?family=Cinzel:wght@400&family=Righteous&family=Saira+Condensed:wght@700&family=Tinos&display=swap" rel="stylesheet">
<style>
  :root {
    --stage: #cfcfcf;
    --stage-light: #e4e4e4;
    --cover: #1c1c1c;
    --cover-edge: #2a2a2a;
    --ink-light: #ffffff;
    --band: #e9e9e7;
    --band-ink: #1a1a1a;
    --photo-top: #8a8378;
    --photo-bottom: #cfc8bd;
  }
  * { margin: 0; padding: 0; box-sizing: border-box; }
  html, body { width: 1200px; height: 850px; overflow: hidden; }
  body {
    background: radial-gradient(ellipse at 50% 45%, var(--stage-light), var(--stage) 75%);
    position: relative;
  }

  .front-cover {
    position: absolute;
    left: 215px; top: 135px;
    width: 380px; height: 600px;
    background: var(--cover);
    color: var(--ink-light);
  }
  .front-cover .author {
    position: absolute; top: 48px; left: 0; right: 0;
    text-align: center;
    font-family: 'Cinzel', serif;
    font-size: 22px; letter-spacing: 4px;
  }
  .title-mark {
    position: absolute; top: 150px; left: 32px;
    font-family: 'Righteous', sans-serif;
    font-size: 150px; line-height: 1;
    white-space: nowrap;
    letter-spacing: -14px;
  }
  .title-mark span {
    display: inline-block;
    text-shadow: -3px 2px 6px rgba(0,0,0,0.55);
  }
  .title-mark .l1 { transform: translateY(0); }
  .title-mark .l2 { transform: translateY(38px); }
  .title-mark .l3 { transform: translateY(52px); }
  .title-mark .l4 { transform: translateY(86px); }
  .subtitle {
    position: absolute; top: 365px; left: 52px;
    font-family: 'Saira Condensed', sans-serif;
    font-weight: 700;
    font-size: 33px; line-height: 1.05;
  }
  .subtitle .second { display: block; padding-left: 6px; }

  .back-cover {
    position: absolute;
    left: 625px; top: 135px;
    width: 330px; height: 600px;
    background: var(--cover);
  }
  .author-band {
    position: absolute; left: 30px; top: 0;
    width: 195px; height: 100%;
    background: var(--band);
    color: var(--band-ink);
    padding: 48px 14px 0;
    font-family: 'Tinos', serif;
  }
  .author-photo {
    width: 86px; height: 96px;
    margin-left: 2px;
    background: linear-gradient(180deg, var(--photo-top), var(--photo-bottom));
  }
  .author-band .name { font-size: 13px; margin: 4px 0 16px 2px; }
  .author-band .bio {
    font-size: 11.2px; line-height: 1.17;
    text-align: justify;
  }
  .author-band .bio + .bio { margin-top: 2px; }

  .spine {
    position: absolute;
    left: 955px; top: 135px;
    width: 44px; height: 600px;
    background: var(--cover-edge);
    color: var(--ink-light);
  }
  .spine .spine-author {
    position: absolute; top: 120px; left: 50%;
    transform: translateX(-50%) rotate(90deg);
    transform-origin: center;
    white-space: nowrap;
    font-family: 'Cinzel', serif; font-size: 15px; letter-spacing: 3px;
    margin-top: 40px;
  }
  .spine .spine-title {
    position: absolute; bottom: 70px; left: 50%;
    transform: translateX(-50%) rotate(90deg);
    white-space: nowrap;
    font-family: 'Righteous', sans-serif; font-size: 22px;
  }
</style>
</head>
<body>
  <section class="front-cover">
    <p class="author">Marla Voskin</p>
    <h1 class="title-mark" aria-label="KITE">
      <span class="l1">K</span><span class="l2">I</span><span class="l3">T</span><span class="l4">E</span>
    </h1>
    <p class="subtitle">Turning Crews<span class="second">into Clans.</span></p>
  </section>

  <section class="back-cover">
    <div class="author-band">
      <div class="author-photo" role="img" aria-label="Portrait photograph of the author"></div>
      <p class="name">Marla Voskin</p>
      <p class="bio">Lorem Ipsum is simply dummy text of the printing and typesetting industry. Lorem Ipsum has been the industry's standard dummy text ever since the 1500s, when an unknown printer took a galley of type and scrambled it to make a type specimen book. It has survived not only five centuries, but also the leap into electronic typesetting, remaining essentially unchange.</p>
      <p class="bio">It was popularised in the 1960s with the release of Transfix sheets containing Lorem Ipsum passages, and more recently with desktop publishing software like Pagewright Studio including versions of Lorem Ipsum.</p>
    </div>
  </section>

  <aside class="spine">
    <span class="spine-author">Marla Voskin</span>
    <span class="spine-title">KITE</span>
  </aside>
</body>
</html>
```